Dana's Paw Spruce & Shine

I have a mobile dog grooming business and I need a design. I would like a scruffy dirty dog as a before dog. Then a clean short hair neatly groomed dog as the after been cleaned and groom by my service. Cartoon images would be good.
My services are bathing, drying, cleaning ears, clipping nails, clip and style hair and deodorising. The mobile van is white and my mobile number is 0452631084.
No dog in bath/tub designs please as they are too common.

Target Market(s)

Clients who wish their dogs to be clean and clipped, ready for the summer heat and Christmas where friends and family visit. They want their dog smelling nice and looking good.

Industry/Entity Type

Graphic Design

Contact Information for Business Card

DANA'S PAW SPRUCE & SHINE Mobile Grooming
Bath, Trim Nails, Clean Ears, Style Clip, Blow Dry,
Cologne. Call Us On: 0452631084

Font styles to use
Script

Colors
85cae6
34a6d7
0393ce
ec1f27

Requirements
Must have
• A Logo with a picture of 2 dogs.. One dirty dog, scruffy long hair, messy, neglected
• 2nd Dog, Clean, Hair neat Looking Sharp and well
• looked after.
• A comparison of two dogs the before and after shots of the same dog. Before it was groomed and after it was groomed. Cartoon form.
Nice to have
• The colour of my Van is White with a light blue stripe at the bottom. I would like colours to suit my trailer eg Grey's, Bubbles, or water drops. Red & Black writing.
• As I need business cards and vinyl sticker logo to put on my trailer.
Should not have
• No dogs in baths or tubs as they are too common in the Mobile Grooming Industry.
• Needs to be unique. .

```html
<!DOCTYPE html>
<html lang="en">
<head>
<meta charset="utf-8">
<title>Dana's Paw Spruce &amp; Shine – Business Card</title>
<link rel="stylesheet" href="https://fonts.googleapis.com/css2?family=Exo+2:ital,wght@0,500;0,800;1,700&family=Yellowtail&family=Schoolbell&display=swap">
<style>
  :root {
    --page-grey: #e4e6e8;
    --card-blue: #4d94d6;
    --brand-red: #e31e26;
    --dog-brown: #8a7561;
    --dog-brown-light: #ad9780;
    --label-tan: #c9b89a;
  }
  * { box-sizing: border-box; margin: 0; padding: 0; }
  html, body {
    width: 1200px;
    height: 873px;
    overflow: hidden;
    background: var(--page-grey);
  }
  .business-card {
    position: absolute;
    left: 100px;
    top: 150px;
    width: 1000px;
    height: 572px;
    background: var(--card-blue);
    border-radius: 6px;
    box-shadow: 0 6px 18px rgba(0,0,0,0.18);
    overflow: hidden;
  }
  .business-name {
    position: absolute;
    top: 30px;
    left: 0;
    width: 100%;
    text-align: center;
    font-family: 'Exo 2', sans-serif;
    font-weight: 800;
    font-size: 54px;
    line-height: 64px;
    letter-spacing: 1px;
    color: var(--brand-red);
  }
  .tagline {
    position: absolute;
    top: 98px;
    left: 0;
    width: 100%;
    text-align: center;
    font-family: 'Yellowtail', cursive;
    font-size: 40px;
    line-height: 50px;
    color: var(--brand-red);
  }
  .services {
    position: absolute;
    top: 154px;
    left: 0;
    width: 100%;
    text-align: center;
    font-family: 'Exo 2', sans-serif;
    font-weight: 500;
    font-size: 23px;
    line-height: 30px;
    color: var(--brand-red);
  }
  .dog-art {
    position: absolute;
    border-radius: 28px;
  }
  .dog-art--before {
    left: 70px;
    top: 236px;
    width: 300px;
    height: 190px;
    background: linear-gradient(160deg, var(--dog-brown-light), var(--dog-brown));
  }
  .dog-art--after {
    left: 600px;
    top: 226px;
    width: 270px;
    height: 300px;
    background: linear-gradient(200deg, var(--dog-brown-light), var(--dog-brown));
  }
  .stage-label {
    position: absolute;
    font-family: 'Schoolbell', cursive;
    font-size: 26px;
    line-height: 30px;
    color: var(--label-tan);
  }
  .stage-label--before { left: 84px; top: 200px; }
  .stage-label--after { left: 884px; top: 480px; }
  .phone-icon {
    position: absolute;
    left: 440px;
    top: 268px;
    width: 84px;
    height: 84px;
  }
  .phone-number {
    position: absolute;
    top: 450px;
    left: 60px;
    width: 480px;
    text-align: center;
    font-family: 'Exo 2', sans-serif;
    font-weight: 700;
    font-style: italic;
    font-size: 50px;
    line-height: 60px;
    color: var(--brand-red);
  }
</style>
</head>
<body>
  <main class="business-card">
    <h1 class="business-name">DANA'S PAW SPRUCE &amp; SHINE</h1>
    <p class="tagline">Mobile Grooming Bath</p>
    <p class="services">Trim Nails, Clean Ears, Style Clip, Blow Dry, Cologne</p>

    <span class="stage-label stage-label--before">before...</span>
    <div class="dog-art dog-art--before" role="img" aria-label="Cartoon of a scruffy, dirty long-haired dog before grooming"></div>

    <svg class="phone-icon" viewBox="0 0 84 84" role="img" aria-label="Phone">
      <circle cx="42" cy="42" r="37" fill="none" stroke="var(--brand-red)" stroke-width="6"/>
      <path d="M30 22 q-8 4 -6 16 q4 16 18 24 q10 5 16 -2 l-7 -8 q-4 3 -8 0 q-8 -6 -10 -14 q-1 -4 3 -6 z"
            fill="var(--brand-red)"/>
    </svg>
    <p class="phone-number">0452631084</p>

    <div class="dog-art dog-art--after" role="img" aria-label="Cartoon of the same dog clean, short-haired and neatly groomed after grooming"></div>
    <span class="stage-label stage-label--after">after...</span>
  </main>
</body>
</html>
```